Foot doctor needs feet friendly business cards.

Business cards for Podiatrist. Needs to look professional and modern. Back side put an appointment card, and try to put a little basic street map somewhere on card along with all of our contact info below:

Marcus Hollend, DPM, Inc.
Diplomate, National Council of Lower Limb Practice
Call: 1.877.Walk.482
1.555.238.6149
Fax: 1.555.871.3902
Email: info@DrHollend.example
Web: www.DrHollend.example
2741 N. Harbor Ln. Suite 208
Bayview Hills, CA 90413

```html
<!DOCTYPE html>
<html lang="en">
<head>
<meta charset="utf-8">
<title>Marcus Hollend, DPM – Business &amp; Appointment Card</title>
<link href="https://fonts.googleapis.com/css2?family=Arimo:wght@400;700&family=Raleway:wght@400;500;700&display=swap" rel="stylesheet">
<style>
  :root {
    --teal-dark: #13708f;
    --teal-light: #5bbcd6;
    --teal-pale: #e6f4f8;
    --card-white: #ffffff;
    --page-bg: #eef0f2;
    --map-base: #e9e5dc;
  }
  * { margin: 0; padding: 0; box-sizing: border-box; }
  html, body { width: 1200px; height: 1000px; overflow: hidden; }
  body { background: var(--page-bg); position: relative; font-family: "Arimo", Arial, sans-serif; color: var(--teal-dark); }

  .card {
    position: absolute; left: 265px; width: 666px; height: 398px;
    background: var(--card-white); border-radius: 22px; overflow: hidden;
    box-shadow: 0 2px 6px rgba(0,0,0,0.15);
  }
  .card--front { top: 73px; }
  .card--back { top: 532px; }
  .abs { position: absolute; white-space: nowrap; }

  /* Front */
  .brand-mark { left: 32px; top: 34px; width: 100px; height: 100px; border-radius: 50%; border: 5px solid var(--teal-dark); background: var(--teal-light); }
  .brand-name { left: 143px; top: 54px; font-size: 27px; font-weight: 700; color: var(--teal-dark); letter-spacing: -0.3px; }
  .brand-role { left: 199px; top: 94px; font-size: 19px; font-weight: 700; letter-spacing: 5.6px; color: var(--teal-light); }
  .doctor-name { right: 32px; top: 168px; font-family: "Raleway", sans-serif; font-size: 24px; font-weight: 700; }
  .doctor-title { right: 32px; top: 199px; font-family: "Raleway", sans-serif; font-size: 17px; color: var(--teal-light); }
  .rule-light { left: 32px; top: 225px; width: 230px; height: 1.5px; background: var(--teal-light); }
  .rule-dark { left: 258px; top: 224px; width: 376px; height: 2.5px; background: var(--teal-dark); }
  .contact-list { left: 32px; top: 244px; list-style: none; }
  .contact-list li { display: flex; align-items: center; height: 27.5px; font-size: 17px; }
  .contact-list svg { width: 20px; height: 20px; margin-right: 9px; }
  .call-line { right: 32px; top: 265px; font-size: 19px; }
  .call-line strong { font-weight: 700; }
  .address { right: 32px; top: 303px; font-size: 17px; text-align: right; line-height: 23px; }
  .band-light { left: 0; top: 359px; width: 100%; height: 6px; background: var(--teal-light); }
  .band-dark { left: 0; top: 365px; width: 100%; height: 33px; background: var(--teal-dark); }

  /* Back */
  .back-header { left: 0; top: 0; width: 100%; height: 114px; background: var(--teal-dark); }
  .back-header-rule { left: 0; top: 116px; width: 373px; height: 2px; background: var(--teal-light); }
  .back-mark { left: 33px; top: 32px; width: 72px; height: 72px; border-radius: 50%; border: 4px solid var(--card-white); background: var(--teal-dark); }
  .back-name { left: 112px; top: 47px; font-size: 17.5px; font-weight: 700; color: var(--card-white); }
  .back-role { left: 153px; top: 76px; font-size: 13px; font-weight: 700; letter-spacing: 4px; color: var(--card-white); }
  .faint-ring { left: 90px; top: 150px; width: 200px; height: 200px; border-radius: 50%; border: 14px solid var(--teal-pale); }
  .form-field { font-family: "Raleway", sans-serif; font-size: 17.5px; font-weight: 700; }
  .form-line { height: 1.5px; background: var(--teal-light); }
  .reminder { left: 32px; top: 324px; font-family: "Raleway", sans-serif; font-size: 16.5px; line-height: 24px; }
  .reminder strong { font-weight: 700; }
  .map-frame { left: 373px; top: 31px; width: 262px; height: 336px; background: var(--teal-light); padding: 6px; }
  .map-area { width: 100%; height: 100%; background: linear-gradient(160deg, var(--map-base) 0%, #e3ddd2 60%, #f2d9a6 100%); }
</style>
</head>
<body>

<section class="card card--front" aria-label="Business card front">
  <div class="abs brand-mark" aria-hidden="true"></div>
  <div class="abs brand-name">Marcus Hollend, DPM, Inc.</div>
  <div class="abs brand-role">PODIATRIST</div>

  <div class="abs doctor-name">Dr. Marcus Hollend</div>
  <div class="abs doctor-title">Diplomate, National Council of Lower Limb Practice</div>
  <div class="abs rule-light"></div>
  <div class="abs rule-dark"></div>

  <ul class="abs contact-list">
    <li>
      <svg viewBox="0 0 20 20" aria-hidden="true"><circle cx="10" cy="10" r="9" fill="none" stroke="var(--teal-dark)" stroke-width="1.5"/><path d="M6.5 5.5c.8-.6 1.6-.4 2 .3l.8 1.5c.3.6 0 1-.5 1.4.5 1.2 1.4 2.1 2.5 2.6.4-.5.8-.8 1.4-.5l1.5.8c.7.4.8 1.2.2 2-1.8 1.8-8.6-4.3-7.9-8.1z" fill="var(--teal-dark)"/></svg>
      1.555.238.6149
    </li>
    <li>
      <svg viewBox="0 0 20 20" aria-hidden="true"><circle cx="10" cy="10" r="9" fill="none" stroke="var(--teal-dark)" stroke-width="1.5"/><rect x="7" y="4.5" width="6" height="3.5" fill="var(--teal-dark)"/><rect x="4.5" y="8" width="11" height="5" rx="1" fill="var(--teal-dark)"/><rect x="7" y="12" width="6" height="3.5" fill="var(--card-white)" stroke="var(--teal-dark)" stroke-width="1"/></svg>
      1.555.871.3902
    </li>
    <li>
      <svg viewBox="0 0 20 20" aria-hidden="true"><circle cx="10" cy="10" r="9" fill="none" stroke="var(--teal-dark)" stroke-width="1.5"/><rect x="5" y="6.5" width="10" height="7" fill="none" stroke="var(--teal-dark)" stroke-width="1.3"/><path d="M5 6.5l5 4 5-4" fill="none" stroke="var(--teal-dark)" stroke-width="1.3"/></svg>
      info@DrHollend.example
    </li>
    <li>
      <svg viewBox="0 0 20 20" aria-hidden="true"><circle cx="10" cy="10" r="9" fill="none" stroke="var(--teal-dark)" stroke-width="1.5"/><circle cx="10" cy="10" r="5.5" fill="none" stroke="var(--teal-dark)" stroke-width="1.2"/><path d="M4.5 10h11M10 4.5c-2.5 3-2.5 8 0 11M10 4.5c2.5 3 2.5 8 0 11" fill="none" stroke="var(--teal-dark)" stroke-width="1"/></svg>
      www.DrHollend.example
    </li>
  </ul>

  <div class="abs call-line"><strong>Call</strong> 1.877.Walk.482</div>
  <div class="abs address">2741 N. Harbor Ln. Suite 208<br>Bayview Hills, CA 90413</div>

  <div class="abs band-light"></div>
  <div class="abs band-dark"></div>
</section>

<section class="card card--back" aria-label="Appointment card back">
  <div class="abs back-header"></div>
  <div class="abs back-header-rule"></div>
  <div class="abs back-mark" aria-hidden="true"></div>
  <div class="abs back-name">Marcus Hollend, DPM, Inc.</div>
  <div class="abs back-role">PODIATRIST</div>

  <div class="abs faint-ring" aria-hidden="true"></div>

  <div class="abs form-field" style="left:32px; top:176px;">Name</div>
  <div class="abs form-line" style="left:91px; top:191px; width:260px;"></div>
  <div class="abs form-field" style="left:32px; top:228px;">Date</div>
  <div class="abs form-line" style="left:80px; top:243px; width:272px;"></div>
  <div class="abs form-field" style="left:32px; top:280px;">Time</div>
  <div class="abs form-line" style="left:77px; top:295px; width:201px;"></div>
  <div class="abs form-field" style="left:283px; top:280px;">am/pm</div>

  <div class="abs reminder">
    If you’re unable to keep your appointment<br>
    Please call us asap at:
    <svg width="13" height="13" viewBox="0 0 20 20" aria-hidden="true" style="vertical-align:-1px;"><path d="M3 2.5c1.2-.9 2.4-.6 3 .4l1.2 2.3c.5.9 0 1.5-.7 2.1.8 1.8 2.1 3.1 3.8 3.9.6-.7 1.2-1.2 2.1-.7l2.3 1.2c1 .6 1.2 1.8.3 3C12.3 17.4 2 8.3 3 2.5z" fill="var(--teal-dark)"/></svg>
    <strong>555.333.7182</strong>
  </div>

  <div class="abs map-frame">
    <div class="map-area" role="img" aria-label="Basic street map showing the office location near the freeway interchange"></div>
  </div>
</section>

</body>
</html>
```